Creative, Modern and Conversion based Web Design

Kovel Digital has recently launched a new logo and as part of our companies rebranding, we need a new website aimed towards the UK B2B marketplace.

The website needs to deliver a modern and creative website design whilst ensuring the design is tailored towards conversion optimisation.

This site must drive point of contact either from an online form, via a direct telephone call or Skype connection.

Our sales are all offline so the website will be a simple, elegant and stunning information portal.

Kovel Digital offers Digital Marketing services to companies throughout the UK - our target audiences are companies that turnover a minimum of 3 million pounds a year and as such we need to deliver a professional image that installs confidence in our companies abilities.

We do not like websites that are reliant upon stock photography - we are happy for stock photography to be used in a small way however the site must not look like a template filled with stock photography.

What do we do

We supply digital marketing services to those companies who demand a strong return on investment - our company prides itself on delivering successful campaigns that help establish long-term profitable relationships.

A lot of the information presented on our old site is relevant today however the design sucks. So please use the information on our current website as a foundation for your design content.

I am looking for several page designs including

"Home Page" Desktop Version
"Service Page" Desktop Version
"Blog Page" Desktop Version

"Home Page" Mobile Version
"Service Page" Mobile Version
"Blog Page" Mobile Version

In the 1st instance please only submit a single design for the "Home Page" Desktop Version - those designers that we are impressed with will be asked to complete the other designs before a winner is selected.

I like modern clean fonts - the site needs to welcome the reader and encourage them to absorb the information - not to overload and make them leave.

The site must be designed to naturally fit our companies new logo.

NO TEMPLATES

Target Market(s)

B2b - 3 million turnover and above

Industry/Entity Type

Digital Marketing

Number of Pages Required

3 page

Requirements
Must have
• Blended well with the companies logo
• We need conversion optimisation to be a huge part of the design - we considered a conversation when a potential customer reaches out to use via - web form, telephone or skype
• The current content on the old website fits today's business but the design sucks.
• www.koveldigital-studio.net
Nice to have
• We need 3 pages (in 2 variants Desktop and Mobile)
• Home Page
• Service Page
• Blog Page
• Please only deliver the "Home Page" desktop version - if we are happy with your design we will aks for the additional pages
Should not have
• No templates and not stock photo heavy design

```html
<!DOCTYPE html>
<html lang="en">
<head>
<meta charset="utf-8">
<title>Kovel Digital LTD – Search Marketing</title>
<link href="https://fonts.googleapis.com/css2?family=Lato:wght@400;700;900&display=swap" rel="stylesheet">
<style>
:root{
  --blue:#1b6fe3;
  --blue-dark:#0c4fb4;
  --blue-deep:#0a3f98;
  --blue-light:#eaf2fc;
  --ink:#1e2430;
  --grey:#6f7682;
  --line:#c9d3e0;
  --white:#ffffff;
}
*{box-sizing:border-box;margin:0;padding:0}
html,body{width:1200px;height:4467px;overflow:hidden}
body{font-family:'Lato',Arial,sans-serif;color:var(--ink);background:var(--white);position:relative}
.section{position:absolute;left:0;width:1200px}
a{color:inherit;text-decoration:none}
.more{color:var(--blue-dark);font-weight:700;text-decoration:underline}
.section-title{position:absolute;left:0;width:1200px;text-align:center;font-size:32px;font-weight:900;color:var(--ink)}
.section-intro{position:absolute;left:300px;width:600px;text-align:center;font-size:15px;line-height:26px;color:var(--grey)}
.btn{position:absolute;display:flex;align-items:center;justify-content:center;font-size:16px;font-weight:700;border-radius:4px;background:linear-gradient(180deg,var(--blue),var(--blue-dark));color:var(--white)}

/* hero */
.hero{top:0;height:640px}
.hero-bg{position:absolute;left:0;top:0}
.brand{position:absolute;left:84px;top:28px;display:flex;align-items:center;gap:10px;color:var(--white);font-weight:900;font-size:17px;letter-spacing:1px}
.brand-mark{width:22px;height:22px;border:3px solid var(--white)}
.nav{position:absolute;top:40px;left:485px;color:var(--white);font-size:15px}
.nav a{position:absolute;white-space:nowrap}
.nav .active{font-weight:900}
.hero-title{position:absolute;left:84px;top:214px;font-size:40px;color:var(--white);font-weight:400}
.hero-sub{position:absolute;left:84px;top:286px;font-size:19px;font-weight:700;color:var(--white)}
.hero-text{position:absolute;left:84px;top:333px;font-size:14px;color:var(--white)}
.hero-btn{position:absolute;left:84px;top:386px;width:134px;height:52px;border:2px solid var(--white);border-radius:4px;color:var(--white);font-weight:700;font-size:16px;display:flex;align-items:center;justify-content:center}
.hero-art{position:absolute;left:650px;top:90px;width:520px;height:490px;border-radius:40px;background:radial-gradient(circle at 50% 55%,#bfe2ff 0%,#5aa7f2 45%,rgba(27,111,227,0) 75%)}

/* services */
.services{top:640px;height:664px}
.service{position:absolute;width:330px;text-align:center}
.service-icon{width:70px;height:70px;margin:0 auto;border-radius:10px;background:linear-gradient(160deg,#4f9bf5,var(--blue-dark));box-shadow:0 8px 18px rgba(12,79,180,.25);display:flex;align-items:center;justify-content:center}
.service h3{margin-top:28px;font-size:16px;font-weight:900}
.service p{margin-top:10px;font-size:14px;line-height:24px;color:var(--grey)}

/* welcome */
.welcome{top:1304px;height:468px;background:var(--blue-light)}
.welcome-art{position:absolute;left:40px;top:35px;width:400px;height:400px;border-radius:50%;background:radial-gradient(circle,#cfe2fb 0%,#e3eefc 55%,rgba(234,242,252,0) 72%)}
.welcome h2{position:absolute;left:470px;top:140px;font-size:30px;font-weight:900}
.welcome p{position:absolute;left:470px;top:198px;width:700px;font-size:13px;line-height:21px;color:var(--grey)}

/* how */
.how{top:1772px;height:461px}
.how-line{position:absolute;left:238px;top:247px;width:722px;height:2px;background:var(--line)}
.step{position:absolute;width:340px;text-align:center;top:210px}
.step-circle{width:76px;height:76px;margin:0 auto;border-radius:50%;background:var(--white);border:2px solid var(--line);position:relative;display:flex;align-items:center;justify-content:center}
.step-num{position:absolute;left:26px;bottom:-14px;width:24px;height:24px;border-radius:50%;background:var(--blue-dark);color:var(--white);font-size:13px;font-weight:900;display:flex;align-items:center;justify-content:center}
.step h3{margin-top:32px;font-size:16px;font-weight:900}
.step p{margin-top:10px;font-size:14px;line-height:24px;color:var(--grey)}

/* pricing */
.pricing{top:2233px;height:403px;background:var(--blue-light)}
.pricing h2{position:absolute;left:80px;top:60px;font-size:31px;font-weight:900}
.pricing h4{position:absolute;left:80px;top:133px;font-size:15px;font-weight:900}
.pricing p{position:absolute;left:80px;top:183px;width:610px;font-size:14px;line-height:25px;color:var(--grey)}
.price-card{position:absolute;left:760px;top:60px;width:312px;height:262px;border-radius:6px;background:linear-gradient(170deg,#3f8ff2,var(--blue-dark));color:var(--white);text-align:center;box-shadow:0 14px 30px rgba(12,79,180,.3)}
.price-card .grade{margin-top:34px;font-size:16px;font-weight:700}
.price-circle{width:92px;height:92px;margin:18px auto 0;border-radius:50%;border:3px solid var(--white);display:flex;align-items:center;justify-content:center;font-size:30px;font-weight:700}
.price-card .per{margin-top:10px;font-size:13px}
.price-card .stat{font-size:15px;font-weight:700;margin-top:8px}
.arrow{position:absolute;top:195px;font-size:28px;color:var(--blue-dark)}

/* seo */
.seo{top:2636px;height:789px}
.seo h4{position:absolute;left:0;width:1200px;text-align:center;top:124px;font-size:16px;font-weight:900}
.seo .section-intro{left:215px;width:770px;top:165px}
.seo-list-title{position:absolute;left:80px;top:312px;font-size:16px;font-weight:900}
.seo-list{position:absolute;left:80px;top:358px;width:670px;list-style:none}
.seo-list li{position:relative;padding-left:26px;font-size:14px;line-height:26px;color:var(--grey);margin-bottom:30px}
.seo-list li::before{content:"";position:absolute;left:0;top:9px;width:8px;height:8px;border-radius:50%;background:var(--blue)}
.seo-art{position:absolute;left:805px;top:380px;width:345px;height:335px;border-radius:30px;background:linear-gradient(160deg,#e4eefc,#c3d8f7)}

/* contact */
.contact{top:3425px;height:446px;background:var(--blue-light)}
.contact h2{position:absolute;left:0;width:1200px;text-align:center;top:58px;font-size:32px;font-weight:900}
.field{position:absolute;height:34px;border-bottom:1px solid var(--line);font-size:14px;color:var(--grey)}

/* partners */
.partners{top:3871px;height:185px}
.badge{position:absolute;top:62px;height:38px;border-radius:6px;background:#8c939c}

/* footer */
.footer{top:4056px;height:411px;background:linear-gradient(180deg,var(--blue),var(--blue-deep));color:var(--white)}
.f-col{position:absolute;top:52px;font-size:14px;line-height:31px}
.f-col h5{font-size:16px;font-weight:900;margin-bottom:10px}
.f-row{display:flex;gap:12px}
.f-brand{position:absolute;left:946px;top:50px;width:200px;text-align:center;font-size:14px;line-height:23px}
.f-brand .name{display:flex;justify-content:center;align-items:center;gap:8px;font-weight:900;font-size:17px;margin-bottom:16px}
.f-brand .sq{width:18px;height:18px;border:3px solid var(--white)}
.f-divider{position:absolute;left:80px;top:344px;width:1040px;height:1px;background:rgba(255,255,255,.35)}
.f-copy{position:absolute;left:80px;top:367px;font-size:13px}
.f-social{position:absolute;right:80px;top:368px;display:flex;gap:18px}
.f-social span{width:14px;height:14px;border-radius:50%;background:var(--white)}
</style>
</head>
<body>

<header class="section hero">
  <svg class="hero-bg" width="1200" height="640" viewBox="0 0 1200 640" aria-hidden="true">
    <defs><linearGradient id="heroGrad" x1="0" y1="0" x2="1" y2="1"><stop offset="0" stop-color="#2b7ff0"/><stop offset="1" stop-color="#0c4fb4"/></linearGradient></defs>
    <path d="M0 0H1200V70C1080 250 760 470 560 560C420 620 200 620 0 612Z" fill="url(#heroGrad)"/>
  </svg>
  <div class="brand"><span class="brand-mark"></span>KOVEL DIGITAL LTD</div>
  <nav class="nav">
    <a class="active" style="left:0;">Home</a>
    <a style="left:97px;">Services</a>
    <a style="left:215px;">White Label Link Building</a>
    <a style="left:445px;">Contact Us</a>
  </nav>
  <h1 class="hero-title">Search Marketing</h1>
  <div class="hero-sub">That Actually Delivers</div>
  <p class="hero-text">Search marketing is our forte. Our client results highlight just how good we do it.</p>
  <a class="hero-btn">Contact Us</a>
  <div class="hero-art" role="img" aria-label="Isometric illustration of cloud servers and data blocks"></div>
</header>

<section class="section services">
  <h2 class="section-title" style="top:36px;">Our Services</h2>
  <p class="section-intro" style="top:100px;">Lorem Ipsum is simply dummy text of the printing and typesetting industry. Lorem Ipsum has been the industry's standard dummy text ever since the 1500s.</p>

  <div class="service" style="left:80px;top:194px;">
    <div class="service-icon"><svg width="30" height="30" viewBox="0 0 30 30"><circle cx="13" cy="13" r="8" fill="none" stroke="#fff" stroke-width="3"/><path d="M19 19l7 7" stroke="#fff" stroke-width="3"/></svg></div>
    <h3>Organic Search</h3><p>Attract traffic that converts and interacts with your brand through Organic...<a class="more">Read More</a></p>
  </div>
  <div class="service" style="left:435px;top:194px;">
    <div class="service-icon"><svg width="30" height="30" viewBox="0 0 30 30"><circle cx="15" cy="15" r="10" fill="none" stroke="#fff" stroke-width="3"/><path d="M15 9v12M11 13h8" stroke="#fff" stroke-width="2.5"/></svg></div>
    <h3>Paid Search</h3><p>Drive highly converting traffic to your website. Our PPC...<a class="more">Read More</a></p>
  </div>
  <div class="service" style="left:788px;top:194px;">
    <div class="service-icon"><svg width="30" height="30" viewBox="0 0 30 30"><rect x="5" y="7" width="18" height="18" fill="none" stroke="#fff" stroke-width="3"/><path d="M14 16L25 5M18 5h7v7" stroke="#fff" stroke-width="3" fill="none"/></svg></div>
    <h3>Link Outreach</h3><p>The core foundation of any search campaign. Our team of link...<a class="more">Read More</a></p>
  </div>
  <div class="service" style="left:80px;top:426px;">
    <div class="service-icon"><svg width="30" height="30" viewBox="0 0 30 30"><rect x="4" y="6" width="22" height="15" rx="2" fill="none" stroke="#fff" stroke-width="3"/><path d="M11 25h8" stroke="#fff" stroke-width="3"/></svg></div>
    <h3>UX &amp; CRO</h3><p>Let us dig into your analytic channels and identify where we can...<a class="more">Read More</a></p>
  </div>
  <div class="service" style="left:435px;top:426px;">
    <div class="service-icon"><svg width="30" height="30" viewBox="0 0 30 30"><rect x="4" y="7" width="22" height="16" fill="none" stroke="#fff" stroke-width="3"/><path d="M4 8l11 9 11-9" stroke="#fff" stroke-width="2.5" fill="none"/></svg></div>
    <h3>Email Marketing</h3><p>Our targeted email marketing campaigns allow you to segment users...<a class="more">Read More</a></p>
  </div>
  <div class="service" style="left:788px;top:426px;">
    <div class="service-icon"><svg width="30" height="30" viewBox="0 0 30 30"><circle cx="15" cy="10" r="5" fill="#fff"/><path d="M5 26c0-6 4-9 10-9s10 3 10 9z" fill="#fff"/></svg></div>
    <h3>Social Media</h3><p>Your followers are your most loyal customers. Let us develop a...<a class="more">Read More</a></p>
  </div>
</section>

<section class="section welcome">
  <div class="welcome-art" role="img" aria-label="Play button ringed by orbiting channel icons"></div>
  <h2>Welcome To Kovel Digital LTD</h2>
  <p>We know and understand the world of business. We know that ROI is the single most important metric in the marketing world. We've worked within some of the world's largest industries – such as finance, insurance, payday loans and health; where achieving above 100% ROI is often impossible. For us, it's just a challenge that can be overcome. Whether we're working with you to drive your Pay-Per-Click Marketing, Organic Search Marketing (SEO), Email Marketing or Lead Filtering &amp; Delivery – we always have your ROI in mind. That's why we're known as the ROI driven digital agency.</p>
  <a class="btn" style="left:470px;top:360px;width:140px;height:50px;">Contact Us</a>
</section>

<section class="section how">
  <h2 class="section-title" style="top:60px;">How It Works</h2>
  <p class="section-intro" style="top:122px;">Lorem Ipsum is simply dummy text of the printing and typesetting industry. Lorem Ipsum has been the industry's standard dummy text ever since the 1500s.</p>
  <div class="how-line"></div>
  <div class="step" style="left:68px;">
    <div class="step-circle"><svg width="34" height="26" viewBox="0 0 34 26"><circle cx="9" cy="8" r="4" fill="#0c4fb4"/><circle cx="17" cy="6" r="5" fill="#0c4fb4"/><circle cx="25" cy="8" r="4" fill="#0c4fb4"/><path d="M2 23c0-5 3-8 7-8 3 0 5 1 6 3 1-2 3-3 4-3s3 1 4 3c1-2 3-3 5-3 4 0 6 3 6 8z" fill="#0c4fb4"/></svg><span class="step-num">1</span></div>
    <h3>You choose your URLs &amp; Anchors</h3><p>The process starts with you deciding what link strength and quantity you need...<a class="more">Read More</a></p>
  </div>
  <div class="step" style="left:430px;">
    <div class="step-circle"><svg width="30" height="30" viewBox="0 0 30 30"><rect x="5" y="4" width="20" height="22" rx="2" fill="none" stroke="#0c4fb4" stroke-width="3"/><path d="M10 11h10M10 16h10M10 21h6" stroke="#0c4fb4" stroke-width="2.5"/></svg><span class="step-num">2</span></div>
    <h3>We handle the outreach</h3><p>With your URLs and anchor text in hand, our team of outreach...<a class="more">Read More</a></p>
  </div>
  <div class="step" style="left:790px;">
    <div class="step-circle"><svg width="30" height="30" viewBox="0 0 30 30"><rect x="6" y="3" width="18" height="24" rx="2" fill="none" stroke="#0c4fb4" stroke-width="3"/><path d="M10 20v-4M15 20v-8M20 20v-6" stroke="#0c4fb4" stroke-width="3"/></svg><span class="step-num">3</span></div>
    <h3>You get a full report</h3><p>We deliver a full report straight to your email inbox with all of the link...<a class="more">Read More</a></p>
  </div>
</section>

<section class="section pricing">
  <h2>Our Pricing</h2>
  <h4>We handle the content, outreach and placements for you</h4>
  <p>We're trusted by more than 100 SEO agencies in the UK. Our in-house team of outreachers are your trusted partner. Each day, we write content, outreach to dozens of real bloggers and secure link placements. Our outreach service is unique; and designed in such a manner that it abides by the guidelines search engines set. There's no other way of safely building links for your clients that drive sustainable and measurable results.</p>
  <span class="arrow" style="left:712px;color:#b9c4d3;">&#8249;</span>
  <div class="price-card">
    <div class="grade">Link Grade: A</div>
    <div class="price-circle">£150</div>
    <div class="per">Per Link</div>
    <div class="stat" style="margin-top:14px;">Root Domains: 1200+</div>
    <div class="stat">Average DA: 30-70</div>
  </div>
  <span class="arrow" style="left:1100px;">&#8250;</span>
</section>

<section class="section seo">
  <h2 class="section-title" style="top:60px;">Handle SEO Yourself? Perfect.</h2>
  <h4>Hassle-Free Link Placements That Drive Rankings</h4>
  <p class="section-intro">Our link placements are used by some of the world's largest companies in the most difficult industries – such as payday loans, insurance, finance, health and legal. We also offer our link placement service in conjunction with our Organic Search (SEO) offerings; although some of our clients handle their SEO in-house and prefer to use our link placements to bolster their rankings.</p>
  <div class="seo-list-title">Here's how our unique, link acquisition process works:</div>
  <ul class="seo-list">
    <li>We take your clients URLs and their business sector (or your own sites), and we utilise our connections to try and secure a link placement.</li>
    <li>All of the sites we outreach too are 100% genuine – we do not own nor control any of the sites.</li>
    <li>If a webmaster chooses to link to you, it is of their own accord. They have decided to link to you. Thus, you have earned a genuine link.</li>
    <li>We will identify the most relevant page/post on their site, and work with the webmaster to weave your links into their existing content. We will write an additional sentence or two to make sure the anchor text fits in with the content.</li>
  </ul>
  <a class="btn" style="left:80px;top:685px;width:135px;height:48px;">Read More</a>
  <div class="seo-art" role="img" aria-label="Illustration of a person at a laptop beside charts and chat bubbles"></div>
</section>

<section class="section contact">
  <h2>Contact Us</h2>
  <div class="field" style="left:283px;top:155px;width:312px;">Name*</div>
  <div class="field" style="left:625px;top:155px;width:298px;">E-mail*</div>
  <div class="field" style="left:283px;top:209px;width:312px;">Phone*</div>
  <div class="field" style="left:625px;top:209px;width:298px;">Subject</div>
  <div class="field" style="left:283px;top:263px;width:640px;height:60px;">Message</div>
  <a class="btn" style="left:533px;top:342px;width:137px;height:50px;">Submit</a>
</section>

<section class="section partners" aria-label="Partner certifications">
  <span class="badge" style="left:120px;width:160px;"></span>
  <span class="badge" style="left:300px;width:145px;"></span>
  <span class="badge" style="left:472px;width:100px;"></span>
  <span class="badge" style="left:655px;width:105px;"></span>
  <span class="badge" style="left:850px;width:120px;"></span>
  <span class="badge" style="left:1007px;width:95px;"></span>
</section>

<footer class="section footer">
  <div class="f-col" style="left:80px;">
    <h5>Services</h5>
    <div>Organic Search</div><div>Paid Search</div><div>Link Outreach</div><div>UX &amp; CRO</div><div>Email Marketing</div><div>Social Media</div>
  </div>
  <div class="f-col" style="left:348px;">
    <h5>Get In Touch</h5>
    <div class="f-row"><svg width="14" height="18" viewBox="0 0 14 18" style="margin-top:6px"><path d="M7 0a7 7 0 0 1 7 7c0 5-7 11-7 11S0 12 0 7a7 7 0 0 1 7-7z" fill="#fff"/><circle cx="7" cy="7" r="2.5" fill="#1b6fe3"/></svg><div style="line-height:23px;margin-top:4px;">Kovel Digital Ltd<br>Unit 4 Larkfield Works<br>Mercer Lane<br>Hollinford<br>HF2 7QX</div></div>
    <div class="f-row" style="margin-top:12px;"><svg width="14" height="14" viewBox="0 0 14 14" style="margin-top:9px"><path d="M3 0l3 3-2 2c1 2 3 4 5 5l2-2 3 3-2 3C6 14 0 8 0 3z" fill="#fff"/></svg><span>01632 960418</span></div>
    <div class="f-row" style="margin-top:8px;"><svg width="14" height="11" viewBox="0 0 14 11" style="margin-top:10px"><rect width="14" height="11" fill="#fff"/><path d="M0 0l7 6 7-6" stroke="#1b6fe3" fill="none"/></svg><span>hello@koveldigital-studio.net</span></div>
  </div>
  <div class="f-col" style="left:620px;">
    <h5>Locations We Cover</h5>
    <div>Birmingham</div><div>Essex</div><div>London</div><div>Manchester</div><div>Stoke-on-Trent</div>
    <div style="font-weight:700;margin-top:6px;">See All Locations &nbsp;&#8594;</div>
  </div>
  <div class="f-brand">
    <div class="name"><span class="sq"></span>KOVEL DIGITAL</div>
    Lorem Ipsum is simply dummy text of the printing and typesetting industry. Lorem Ipsum has been the industry's standard dummy text ever since the 1500s.
  </div>
  <div class="f-divider"></div>
  <div class="f-copy">© KOVEL DIGITAL LTD - 2018. All Rights Reserved.</div>
  <div class="f-social"><span></span><span></span><span></span><span></span><span></span></div>
</footer>

</body>
</html>
```